Pebble and Pine App design

I need a full app design, colours, images, fonts, and a mock up design of the app to bring to the developer.

Pebble and Pine is a free app that allows cafes, independent cafe and chains of cafes to let their customers know what the soup of the day and what specials they have on that day through the app. Each cafe will have a profile which they can upload the Pebble and Pine daily.

The user home screen will include google maps showing their location with the registered cafes and eateries around them. including a list of the cafe and distances below. as seen in attachment.

Target Market(s)

Cafes , anyone who enjoys eating soups and off local cafe specials boards

Requirements
Must have
• I would like a complete app design based on the attached images.

```html
<!DOCTYPE html>
<html lang="en">
<head>
<meta charset="utf-8">
<title>Pebble and Pine – App Screens</title>
<link href="https://fonts.googleapis.com/css2?family=Roboto:wght@400;500;700&display=swap" rel="stylesheet">
<style>
:root{
  --pink:#f5446a;
  --pink-soft:#fde8ed;
  --bg:#e3e6e9;
  --navy:#1b2a4e;
  --ink:#1e1e1e;
  --muted:#6b6b6b;
  --grey-icon:#b9bcc2;
  --star:#ffc20e;
  --white:#ffffff;
  --page:#f4f5f7;
}
*{box-sizing:border-box;margin:0;padding:0}
html,body{width:1200px;height:804px;overflow:hidden}
body{background:var(--bg);font-family:"Roboto",Arial,sans-serif;position:relative;color:var(--ink)}
.screen{position:absolute;top:103px;width:277px;height:597px;border-radius:30px;background:var(--page);overflow:hidden;box-shadow:0 10px 30px rgba(0,0,0,.12)}
.screen--map{left:93px}
.screen--soups{left:461px}
.screen--specials{left:830px}

.app-header{position:absolute;left:0;top:0;width:100%;height:108px;background:var(--pink);color:var(--white)}
.status-time{position:absolute;left:22px;top:9px;font-size:12px;font-weight:500}
.status-icons{position:absolute;right:18px;top:11px}
.header-back{position:absolute;left:13px;top:39px}
.header-menu{position:absolute;right:13px;top:38px}
.header-title{position:absolute;left:0;right:0;top:37px;text-align:center;font-size:14.5px;font-weight:500}
.search-box{position:absolute;left:12px;right:12px;top:68px;height:30px;border-radius:4px;background:var(--white);display:flex;align-items:center;padding-left:14px;gap:10px;font-size:8.5px;color:#333}

.map-area{position:absolute;left:0;top:108px;width:100%;height:214px;background:linear-gradient(135deg,#e9ebee,#dcdfe3 60%,#e6e8eb)}

.venue-card{position:absolute;left:12px;right:12px;height:83px;background:var(--white);border-radius:4px;display:flex;box-shadow:0 1px 4px rgba(0,0,0,.05)}
.venue-card--one{top:334px}
.venue-card--two{top:428px}
.venue-photo{width:96px;height:100%;flex:none}
.venue-photo--bar{background:linear-gradient(160deg,#1d3e4e,#4a3b33 60%,#7b4b3a)}
.venue-photo--dining{background:linear-gradient(160deg,#3b2a20,#7a5436 55%,#a37551)}
.venue-info{padding:8px 0 0 19px;flex:1}
.venue-name{font-size:12px;font-weight:700;color:var(--navy)}
.venue-type{font-size:8px;color:var(--muted);margin-top:3px}
.stars{color:var(--star);font-size:9px;letter-spacing:1px;line-height:1}
.venue-info .stars{margin-top:3px}
.venue-meta{display:flex;gap:16px;margin-top:6px}
.meta-item{display:flex;align-items:center;gap:6px}
.meta-label{font-size:6.5px;color:var(--muted)}
.meta-value{font-size:8.5px;font-weight:500;color:#111;margin-top:2px}

.dish-grid{position:absolute;left:12px;top:119px;width:254px}
.dish-card{position:absolute;width:121px;height:155px;background:var(--white);border-radius:3px;overflow:hidden;box-shadow:0 1px 4px rgba(0,0,0,.05)}
.dish-card.col-2{left:133px}
.dish-card.row-2{top:166px}
.dish-card.row-3{top:335px}
.dish-photo{position:relative;height:95px}
.fav{position:absolute;right:5px;top:5px;width:15px;height:15px;border-radius:50%;background:var(--white);display:flex;align-items:center;justify-content:center}
.dish-name{font-size:12px;font-weight:500;padding:6px 0 0 5px;color:#111}
.dish-kind{font-size:8px;color:var(--muted);padding:3px 0 0 5px}
.dish-foot{display:flex;justify-content:space-between;align-items:center;padding:6px 4px 0 6px}
.order-btn{width:42px;height:16px;border-radius:3px;background:var(--pink-soft);color:var(--pink);font-size:8.5px;display:flex;align-items:center;justify-content:center}

.p-yellow{background:radial-gradient(circle at 50% 50%,#f7b500 0 30%,#f2f2f2 32% 45%,#9a9a9a 100%)}
.p-cream{background:radial-gradient(circle at 50% 45%,#e9a456 0 30%,#f3f0ea 32% 42%,#6e5a44 100%)}
.p-tomato{background:radial-gradient(circle at 40% 50%,#d9371d 0 28%,#f2f2f2 30% 38%,#3a3a3a 100%)}
.p-veg{background:radial-gradient(circle at 50% 50%,#e8d4a0 0 30%,#f4f1ea 32% 45%,#c9c2b4 100%)}
.p-green{background:linear-gradient(170deg,#7b8895,#b6c48a 60%,#5d6a4a)}
.p-orange{background:radial-gradient(circle at 50% 55%,#f2a31a 0 32%,#f0ebe4 34% 44%,#8a5e44 100%)}
.p-fish{background:radial-gradient(circle at 50% 50%,#e0a54a 0 30%,#f7f7f7 32% 45%,#c3d4e0 100%)}
.p-salsa{background:radial-gradient(circle at 50% 50%,#b8321c 0 28%,#f4f4f4 30% 40%,#6a4a2c 100%)}
.p-chips{background:radial-gradient(circle at 55% 55%,#f3dc7a 0 30%,#f5f5f5 32% 45%,#a9b99a 100%)}
.p-bread{background:radial-gradient(circle at 50% 50%,#a0662e 0 30%,#e8dcc8 32% 60%,#d9cdb8 100%)}
.p-plate{background:radial-gradient(circle at 50% 55%,#d9cbb0 0 16%,#f3f3f3 18% 40%,#b9b2aa 100%)}
.p-fries{background:linear-gradient(150deg,#7a5a36,#e3b056 55%,#d8d0c2)}

.bottom-nav{position:absolute;left:0;bottom:0;width:100%;height:63px;background:var(--white);box-shadow:0 -2px 8px rgba(0,0,0,.05)}
.nav-bump{position:absolute;left:50%;top:-14px;width:66px;height:66px;margin-left:-33px;border-radius:50%;background:var(--white)}
.cart-btn{position:absolute;left:50%;top:-7px;width:41px;height:41px;margin-left:-20.5px;border-radius:50%;background:var(--pink);display:flex;align-items:center;justify-content:center;box-shadow:0 3px 8px rgba(245,68,106,.35)}
.nav-item{position:absolute;top:13px;width:50px;text-align:center;font-size:8.5px;color:var(--grey-icon)}
.nav-item svg{display:block;margin:0 auto 3px}
.nav-item.is-active{color:var(--pink)}
.nav-1{left:3px}.nav-2{left:55px}.nav-3{left:176px}.nav-4{left:224px}
.home-bar{position:absolute;left:50%;bottom:6px;width:102px;height:3px;margin-left:-51px;border-radius:2px;background:#111}
</style>
</head>
<body>

<!-- Screen 1: Nearby -->
<section class="screen screen--map">
  <header class="app-header">
    <span class="status-time">9:41</span>
    <svg class="status-icons" width="38" height="8" viewBox="0 0 38 8"><rect x="0" y="5" width="2" height="3" fill="#fff"/><rect x="3" y="3.5" width="2" height="4.5" fill="#fff"/><rect x="6" y="2" width="2" height="6" fill="#fff"/><path d="M13 4a5 5 0 0 1 7 0M14.5 5.7a3 3 0 0 1 4 0" stroke="#fff" stroke-width="1.2" fill="none"/><circle cx="16.5" cy="7.2" r=".8" fill="#fff"/><rect x="25" y="1.5" width="12" height="5.5" rx="1.3" fill="#fff"/></svg>
    <svg class="header-back" width="15" height="10" viewBox="0 0 15 10"><path d="M14 5H2M5.5 1.5 2 5l3.5 3.5" stroke="#fff" stroke-width="1.8" fill="none"/></svg>
    <svg class="header-menu" width="13" height="11" viewBox="0 0 13 11"><rect width="13" height="2" fill="#fff"/><rect y="4.5" width="13" height="2" fill="#fff"/><rect y="9" width="13" height="2" fill="#fff"/></svg>
    <h1 class="header-title">Nearby Restaurant</h1>
    <div class="search-box"><svg width="10" height="10" viewBox="0 0 10 10"><circle cx="4" cy="4" r="3" stroke="#444" stroke-width="1.5" fill="none"/><path d="M6.3 6.3 9 9" stroke="#444" stroke-width="1.6"/></svg>Nearby Restaurant</div>
  </header>
  <div class="map-area" role="img" aria-label="Street map showing the user's location and nearby registered cafes"></div>

  <article class="venue-card venue-card--one">
    <div class="venue-photo venue-photo--bar" role="img" aria-label="Photo of a cafe counter interior"></div>
    <div class="venue-info">
      <h2 class="venue-name">BBQ Hotless&nbsp; Soup</h2>
      <p class="venue-type">Pebble and Pine</p>
      <div class="stars">★★★★★</div>
      <div class="venue-meta">
        <div class="meta-item"><svg width="7" height="10" viewBox="0 0 7 10"><path d="M3.5 0A3.5 3.5 0 0 0 0 3.5C0 6 3.5 10 3.5 10S7 6 7 3.5A3.5 3.5 0 0 0 3.5 0z" fill="#333"/><circle cx="3.5" cy="3.5" r="1.3" fill="#fff"/></svg><div><div class="meta-label">Distance</div><div class="meta-value">0.500Km</div></div></div>
        <div class="meta-item"><svg width="10" height="10" viewBox="0 0 10 10"><circle cx="5" cy="5" r="4.2" stroke="#333" stroke-width="1.3" fill="none"/><path d="M5 2.6V5h2" stroke="#333" stroke-width="1.2" fill="none"/></svg><div><div class="meta-label">Time</div><div class="meta-value">10 Mins</div></div></div>
      </div>
    </div>
  </article>

  <article class="venue-card venue-card--two">
    <div class="venue-photo venue-photo--dining" role="img" aria-label="Photo of a wooden cafe dining room"></div>
    <div class="venue-info">
      <h2 class="venue-name">Lorem ipsum dolor sit</h2>
      <p class="venue-type">Pebble and Pine</p>
      <div class="stars">★★★★★</div>
      <div class="venue-meta">
        <div class="meta-item"><svg width="7" height="10" viewBox="0 0 7 10"><path d="M3.5 0A3.5 3.5 0 0 0 0 3.5C0 6 3.5 10 3.5 10S7 6 7 3.5A3.5 3.5 0 0 0 3.5 0z" fill="#333"/><circle cx="3.5" cy="3.5" r="1.3" fill="#fff"/></svg><div><div class="meta-label">Distance</div><div class="meta-value">0.500Km</div></div></div>
        <div class="meta-item"><svg width="10" height="10" viewBox="0 0 10 10"><circle cx="5" cy="5" r="4.2" stroke="#333" stroke-width="1.3" fill="none"/><path d="M5 2.6V5h2" stroke="#333" stroke-width="1.2" fill="none"/></svg><div><div class="meta-label">Time</div><div class="meta-value">10 Mins</div></div></div>
      </div>
    </div>
  </article>

  <nav class="bottom-nav">
    <div class="nav-bump"></div>
    <div class="cart-btn"><svg width="20" height="17" viewBox="0 0 20 17"><path d="M1 1.5h3l2.2 9.5h10L18.5 4H5" stroke="#fff" stroke-width="2" fill="none" stroke-linejoin="round"/><circle cx="7.5" cy="14.5" r="1.6" fill="#fff"/><circle cx="15" cy="14.5" r="1.6" fill="#fff"/></svg></div>
    <div class="nav-item nav-1 is-active"><svg width="18" height="16" viewBox="0 0 18 16"><path d="M1 7h16a8 8 0 0 1-16 0z" fill="currentColor"/><path d="M8 1v4M11 1v4M14 1v4" stroke="currentColor" stroke-width="1.2"/></svg>Soups</div>
    <div class="nav-item nav-2"><svg width="16" height="17" viewBox="0 0 16 17"><rect x="2" y="1" width="12" height="15" rx="1" fill="currentColor"/><path d="M4.5 5h7M4.5 8.5h7M4.5 12h5" stroke="#fff" stroke-width="1.3"/></svg>Specials</div>
    <div class="nav-item nav-3"><svg width="16" height="17" viewBox="0 0 16 17"><circle cx="8" cy="5" r="4" fill="currentColor"/><path d="M1 17a7 7 0 0 1 14 0z" fill="currentColor"/></svg>Account</div>
    <div class="nav-item nav-4"><svg width="17" height="17" viewBox="0 0 17 17"><circle cx="8.5" cy="8.5" r="5.5" stroke="currentColor" stroke-width="3.5" stroke-dasharray="2.6 1.7" fill="none"/><circle cx="8.5" cy="8.5" r="3.5" stroke="currentColor" stroke-width="2" fill="none"/></svg>Settings</div>
    <div class="home-bar"></div>
  </nav>
</section>

<!-- Screen 2: Soups -->
<section class="screen screen--soups">
  <header class="app-header">
    <span class="status-time">9:41</span>
    <svg class="status-icons" width="38" height="8" viewBox="0 0 38 8"><rect x="0" y="5" width="2" height="3" fill="#fff"/><rect x="3" y="3.5" width="2" height="4.5" fill="#fff"/><rect x="6" y="2" width="2" height="6" fill="#fff"/><path d="M13 4a5 5 0 0 1 7 0M14.5 5.7a3 3 0 0 1 4 0" stroke="#fff" stroke-width="1.2" fill="none"/><circle cx="16.5" cy="7.2" r=".8" fill="#fff"/><rect x="25" y="1.5" width="12" height="5.5" rx="1.3" fill="#fff"/></svg>
    <svg class="header-back" width="15" height="10" viewBox="0 0 15 10"><path d="M14 5H2M5.5 1.5 2 5l3.5 3.5" stroke="#fff" stroke-width="1.8" fill="none"/></svg>
    <svg class="header-menu" width="13" height="11" viewBox="0 0 13 11"><rect width="13" height="2" fill="#fff"/><rect y="4.5" width="13" height="2" fill="#fff"/><rect y="9" width="13" height="2" fill="#fff"/></svg>
    <h1 class="header-title">Soups</h1>
    <div class="search-box"><svg width="10" height="10" viewBox="0 0 10 10"><circle cx="4" cy="4" r="3" stroke="#444" stroke-width="1.5" fill="none"/><path d="M6.3 6.3 9 9" stroke="#444" stroke-width="1.6"/></svg>Search Soups</div>
  </header>

  <div class="dish-grid">
    <article class="dish-card"><div class="dish-photo p-yellow" role="img" aria-label="Bowl of yellow carrot soup"><span class="fav"><svg width="9" height="8" viewBox="0 0 9 8"><path d="M4.5 7.3 1 4A2 2 0 0 1 4.5 1.3 2 2 0 0 1 8 4z" stroke="#222" stroke-width=".9" fill="none"/></svg></span></div><h3 class="dish-name">Carrot + Curiader</h3><p class="dish-kind">Korean BBQ</p><div class="dish-foot"><span class="stars">★★★★★</span><span class="order-btn">Order</span></div></article>
    <article class="dish-card col-2"><div class="dish-photo p-cream" role="img" aria-label="Bowl of creamy soup with bread"><span class="fav"><svg width="9" height="8" viewBox="0 0 9 8"><path d="M4.5 7.3 1 4A2 2 0 0 1 4.5 1.3 2 2 0 0 1 8 4z" stroke="#222" stroke-width=".9" fill="none"/></svg></span></div><h3 class="dish-name">Carrot + Curiader</h3><p class="dish-kind">Korean BBQ</p><div class="dish-foot"><span class="stars">★★★★★</span><span class="order-btn">Order</span></div></article>
    <article class="dish-card row-2"><div class="dish-photo p-tomato" role="img" aria-label="Bowl of tomato soup with basil"><span class="fav"><svg width="9" height="8" viewBox="0 0 9 8"><path d="M4.5 7.3 1 4A2 2 0 0 1 4.5 1.3 2 2 0 0 1 8 4z" stroke="#222" stroke-width=".9" fill="none"/></svg></span></div><h3 class="dish-name">Carrot + Curiader</h3><p class="dish-kind">Korean BBQ</p><div class="dish-foot"><span class="stars">★★★★★</span><span class="order-btn">Order</span></div></article>
    <article class="dish-card col-2 row-2"><div class="dish-photo p-veg" role="img" aria-label="Bowl of chicken vegetable soup"><span class="fav"><svg width="9" height="8" viewBox="0 0 9 8"><path d="M4.5 7.3 1 4A2 2 0 0 1 4.5 1.3 2 2 0 0 1 8 4z" stroke="#222" stroke-width=".9" fill="none"/></svg></span></div><h3 class="dish-name">Carrot + Curiader</h3><p class="dish-kind">Korean BBQ</p><div class="dish-foot"><span class="stars">★★★★★</span><span class="order-btn">Order</span></div></article>
    <article class="dish-card row-3"><div class="dish-photo p-green" role="img" aria-label="Green pea soup with potatoes"><span class="fav"><svg width="9" height="8" viewBox="0 0 9 8"><path d="M4.5 7.3 1 4A2 2 0 0 1 4.5 1.3 2 2 0 0 1 8 4z" stroke="#222" stroke-width=".9" fill="none"/></svg></span></div></article>
    <article class="dish-card col-2 row-3"><div class="dish-photo p-orange" role="img" aria-label="Sweet potato soup in a bowl"><span class="fav"><svg width="9" height="8" viewBox="0 0 9 8"><path d="M4.5 7.3 1 4A2 2 0 0 1 4.5 1.3 2 2 0 0 1 8 4z" stroke="#222" stroke-width=".9" fill="none"/></svg></span></div></article>
  </div>

  <nav class="bottom-nav">
    <div class="nav-bump"></div>
    <div class="cart-btn"><svg width="20" height="17" viewBox="0 0 20 17"><path d="M1 1.5h3l2.2 9.5h10L18.5 4H5" stroke="#fff" stroke-width="2" fill="none" stroke-linejoin="round"/><circle cx="7.5" cy="14.5" r="1.6" fill="#fff"/><circle cx="15" cy="14.5" r="1.6" fill="#fff"/></svg></div>
    <div class="nav-item nav-1 is-active"><svg width="18" height="16" viewBox="0 0 18 16"><path d="M1 7h16a8 8 0 0 1-16 0z" fill="currentColor"/><path d="M8 1v4M11 1v4M14 1v4" stroke="currentColor" stroke-width="1.2"/></svg>Soups</div>
    <div class="nav-item nav-2"><svg width="16" height="17" viewBox="0 0 16 17"><rect x="2" y="1" width="12" height="15" rx="1" fill="currentColor"/><path d="M4.5 5h7M4.5 8.5h7M4.5 12h5" stroke="#fff" stroke-width="1.3"/></svg>Specials</div>
    <div class="nav-item nav-3"><svg width="17" height="17" viewBox="0 0 17 17"><path d="M8.5 1l2.3 4.8 5.2.7-3.8 3.6.9 5.2-4.6-2.5-4.6 2.5.9-5.2L1 6.5l5.2-.7z" fill="currentColor"/></svg>Favourite</div>
    <div class="nav-item nav-4"><svg width="17" height="17" viewBox="0 0 17 17"><circle cx="8.5" cy="8.5" r="5.5" stroke="currentColor" stroke-width="3.5" stroke-dasharray="2.6 1.7" fill="none"/><circle cx="8.5" cy="8.5" r="3.5" stroke="currentColor" stroke-width="2" fill="none"/></svg>Settings</div>
    <div class="home-bar"></div>
  </nav>
</section>

<!-- Screen 3: Specials -->
<section class="screen screen--specials">
  <header class="app-header">
    <span class="status-time">9:41</span>
    <svg class="status-icons" width="38" height="8" viewBox="0 0 38 8"><rect x="0" y="5" width="2" height="3" fill="#fff"/><rect x="3" y="3.5" width="2" height="4.5" fill="#fff"/><rect x="6" y="2" width="2" height="6" fill="#fff"/><path d="M13 4a5 5 0 0 1 7 0M14.5 5.7a3 3 0 0 1 4 0" stroke="#fff" stroke-width="1.2" fill="none"/><circle cx="16.5" cy="7.2" r=".8" fill="#fff"/><rect x="25" y="1.5" width="12" height="5.5" rx="1.3" fill="#fff"/></svg>
    <svg class="header-back" width="15" height="10" viewBox="0 0 15 10"><path d="M14 5H2M5.5 1.5 2 5l3.5 3.5" stroke="#fff" stroke-width="1.8" fill="none"/></svg>
    <svg class="header-menu" width="13" height="11" viewBox="0 0 13 11"><rect width="13" height="2" fill="#fff"/><rect y="4.5" width="13" height="2" fill="#fff"/><rect y="9" width="13" height="2" fill="#fff"/></svg>
    <h1 class="header-title">Specials</h1>
    <div class="search-box"><svg width="10" height="10" viewBox="0 0 10 10"><circle cx="4" cy="4" r="3" stroke="#444" stroke-width="1.5" fill="none"/><path d="M6.3 6.3 9 9" stroke="#444" stroke-width="1.6"/></svg>Search Specials</div>
  </header>

  <div class="dish-grid">
    <article class="dish-card"><div class="dish-photo p-fish" role="img" aria-label="Plate of fried fish and chips"><span class="fav"><svg width="9" height="8" viewBox="0 0 9 8"><path d="M4.5 7.3 1 4A2 2 0 0 1 4.5 1.3 2 2 0 0 1 8 4z" stroke="#222" stroke-width=".9" fill="none"/></svg></span></div><h3 class="dish-name">Lorem ipsum dol</h3><p class="dish-kind">Korean BBQ</p><div class="dish-foot"><span class="stars">★★★★★</span><span class="order-btn">Order</span></div></article>
    <article class="dish-card col-2"><div class="dish-photo p-salsa" role="img" aria-label="Bowl of salsa with tortilla chips"><span class="fav"><svg width="9" height="8" viewBox="0 0 9 8"><path d="M4.5 7.3 1 4A2 2 0 0 1 4.5 1.3 2 2 0 0 1 8 4z" stroke="#222" stroke-width=".9" fill="none"/></svg></span></div><h3 class="dish-name">Lorem ipsum dol</h3><p class="dish-kind">Korean BBQ</p><div class="dish-foot"><span class="stars">★★★★★</span><span class="order-btn">Order</span></div></article>
    <article class="dish-card row-2"><div class="dish-photo p-chips" role="img" aria-label="Bowl of tortilla chips with dips"><span class="fav"><svg width="9" height="8" viewBox="0 0 9 8"><path d="M4.5 7.3 1 4A2 2 0 0 1 4.5 1.3 2 2 0 0 1 8 4z" stroke="#222" stroke-width=".9" fill="none"/></svg></span></div><h3 class="dish-name">Lorem ipsum dol</h3><p class="dish-kind">Korean BBQ</p><div class="dish-foot"><span class="stars">★★★★★</span><span class="order-btn">Order</span></div></article>
    <article class="dish-card col-2 row-2"><div class="dish-photo p-bread" role="img" aria-label="Sesame bread rings on a table"><span class="fav"><svg width="9" height="8" viewBox="0 0 9 8"><path d="M4.5 7.3 1 4A2 2 0 0 1 4.5 1.3 2 2 0 0 1 8 4z" stroke="#222" stroke-width=".9" fill="none"/></svg></span></div><h3 class="dish-name">Lorem ipsum dol</h3><p class="dish-kind">Korean BBQ</p><div class="dish-foot"><span class="stars">★★★★★</span><span class="order-btn">Order</span></div></article>
    <article class="dish-card row-3"><div class="dish-photo p-plate" role="img" aria-label="Plate with toast and egg"><span class="fav"><svg width="9" height="8" viewBox="0 0 9 8"><path d="M4.5 7.3 1 4A2 2 0 0 1 4.5 1.3 2 2 0 0 1 8 4z" stroke="#222" stroke-width=".9" fill="none"/></svg></span></div></article>
    <article class="dish-card col-2 row-3"><div class="dish-photo p-fries" role="img" aria-label="Potato wedges with dip"><span class="fav"><svg width="9" height="8" viewBox="0 0 9 8"><path d="M4.5 7.3 1 4A2 2 0 0 1 4.5 1.3 2 2 0 0 1 8 4z" stroke="#222" stroke-width=".9" fill="none"/></svg></span></div></article>
  </div>

  <nav class="bottom-nav">
    <div class="nav-bump"></div>
    <div class="cart-btn"><svg width="20" height="17" viewBox="0 0 20 17"><path d="M1 1.5h3l2.2 9.5h10L18.5 4H5" stroke="#fff" stroke-width="2" fill="none" stroke-linejoin="round"/><circle cx="7.5" cy="14.5" r="1.6" fill="#fff"/><circle cx="15" cy="14.5" r="1.6" fill="#fff"/></svg></div>
    <div class="nav-item nav-1"><svg width="18" height="16" viewBox="0 0 18 16"><path d="M1 7h16a8 8 0 0 1-16 0z" fill="currentColor"/><path d="M8 1v4M11 1v4M14 1v4" stroke="currentColor" stroke-width="1.2"/></svg>Soups</div>
    <div class="nav-item nav-2 is-active"><svg width="16" height="17" viewBox="0 0 16 17"><rect x="2" y="1" width="12" height="15" rx="1" fill="currentColor"/><path d="M4.5 5h7M4.5 8.5h7M4.5 12h5" stroke="#fff" stroke-width="1.3"/></svg>Specials</div>
    <div class="nav-item nav-3"><svg width="17" height="17" viewBox="0 0 17 17"><path d="M8.5 1l2.3 4.8 5.2.7-3.8 3.6.9 5.2-4.6-2.5-4.6 2.5.9-5.2L1 6.5l5.2-.7z" fill="currentColor"/></svg>Favourite</div>
    <div class="nav-item nav-4"><svg width="17" height="17" viewBox="0 0 17 17"><circle cx="8.5" cy="8.5" r="5.5" stroke="currentColor" stroke-width="3.5" stroke-dasharray="2.6 1.7" fill="none"/><circle cx="8.5" cy="8.5" r="3.5" stroke="currentColor" stroke-width="2" fill="none"/></svg>Settings</div>
    <div class="home-bar"></div>
  </nav>
</section>

</body>
</html>
```